International Life/Work Balance and Personal Growth company needs a new business card

I have got the logo already and need a creative way in putting it together....

Target Market(s)

corporate - business for stress management/work/life balance seminars
anybody else who is interested in living a extraordinary life and is into Wellness and is open to changing habits

Industry/Entity Type

Business

Requirements
Must have
• must include my photo on the front

On the business card.... yes, both sides.... my name Marisol Pettark mobile 0476 581 904 www.dawnquill.com, also the facebook sign and marisol@dawnquill.com as email, also my pic see attachment and logo with slogan

Workplace Wellness Seminars
Stress Management
Law of Attraction w/s
Personal Transformations
Kestrel Yoga and Pilates

slogan: wellness ~ success ~ peace of mind
Nice to have
• I like the colors of the logo so that should match the card. I like flowing contemporary lines....something that has the feeling of peace and upliftment.

Font could be "chalkboard" or something similar....

```html
<!DOCTYPE html>
<html lang="en">
<head>
<meta charset="utf-8">
<title>Dawnquill Business Card</title>
<link href="https://fonts.googleapis.com/css2?family=Open+Sans:ital,wght@0,400;0,600;0,700;1,700&display=swap" rel="stylesheet">
<style>
  :root {
    --bg: #9a9a9a;
    --green: #537b3b;
    --green-dark: #3f6a2c;
    --blue: #0f4c9c;
    --white: #ffffff;
    --ink: #1c1c1c;
    --photo-a: #c98a5e;
    --photo-b: #2a211d;
  }
  * { box-sizing: border-box; margin: 0; padding: 0; }
  html, body { width: 1200px; height: 900px; overflow: hidden; }
  body {
    background: var(--bg);
    font-family: "Open Sans", Arial, sans-serif;
    position: relative;
  }
  .card {
    position: absolute;
    left: 300px;
    width: 600px;
    height: 340px;
    border-radius: 18px;
    overflow: hidden;
    box-shadow: 0 8px 24px rgba(0,0,0,0.25);
  }
  /* back side */
  .card-back { top: 60px; background: var(--green); }
  .card-back .brand {
    position: absolute;
    left: 290px;
    top: 58px;
    color: var(--white);
    font-weight: 600;
    font-size: 50px;
    line-height: 1;
  }
  .services {
    position: absolute;
    left: 300px;
    top: 140px;
    list-style: none;
    color: var(--white);
    font-size: 15px;
    line-height: 26px;
  }
  .services li::before {
    content: "";
    display: inline-block;
    width: 7px; height: 7px;
    border-radius: 50%;
    background: var(--white);
    margin-right: 12px;
    vertical-align: middle;
  }
  /* front side */
  .card-front { top: 460px; background: var(--white); }
  .waves { position: absolute; left: 0; top: 0; }
  .logo {
    position: absolute;
    left: 28px;
    top: 26px;
    display: flex;
    align-items: center;
    gap: 12px;
  }
  .logo-dot { width: 56px; height: 56px; border-radius: 50%; background: var(--green); }
  .logo-name { color: var(--green); font-weight: 700; font-size: 38px; }
  .photo-frame {
    position: absolute;
    left: 172px;
    top: 108px;
    width: 146px;
    height: 142px;
    background: var(--blue);
    padding: 0 6px 6px 0;
  }
  .photo {
    width: 100%;
    height: 100%;
    border: 5px solid var(--green);
    background: radial-gradient(circle at 50% 45%, var(--photo-a) 0%, var(--photo-a) 30%, var(--photo-b) 75%);
  }
  .person {
    position: absolute;
    left: 340px;
    top: 128px;
    color: var(--blue);
    font-style: italic;
    font-weight: 700;
    font-size: 18px;
    text-transform: uppercase;
    letter-spacing: 0.3px;
  }
  .contacts {
    position: absolute;
    left: 340px;
    top: 164px;
    list-style: none;
    font-size: 13.5px;
    color: var(--ink);
  }
  .contacts li { display: flex; align-items: center; gap: 10px; height: 20px; }
  .contacts svg { flex: none; }
  .slogan {
    position: absolute;
    left: 0; right: 0;
    bottom: 14px;
    text-align: center;
    color: var(--white);
    font-style: italic;
    font-weight: 700;
    font-size: 14px;
    text-transform: uppercase;
    letter-spacing: 0.3px;
  }
</style>
</head>
<body>

<section class="card card-back">
  <div class="brand">Dawnquill</div>
  <ul class="services">
    <li>Workplace Wellness Seminars</li>
    <li>Stress Management</li>
    <li>Law of Attraction w/s</li>
    <li>Personal Transformations</li>
    <li>Kestrel Yoga and Pilates</li>
  </ul>
</section>

<section class="card card-front">
  <svg class="waves" width="600" height="340" viewBox="0 0 600 340">
    <path d="M0,212 C150,250 300,266 440,266 C300,274 150,270 0,248 Z" fill="var(--blue)"/>
    <path d="M0,246 C170,276 420,286 600,228 L600,340 L0,340 Z" fill="var(--green)"/>
  </svg>

  <div class="logo">
    <span class="logo-dot"></span>
    <span class="logo-name">Dawnquill</span>
  </div>

  <div class="photo-frame">
    <div class="photo" role="img" aria-label="Portrait photo of Marisol Pettark"></div>
  </div>

  <div class="person">Marisol Pettark</div>
  <ul class="contacts">
    <li>
      <svg width="14" height="14" viewBox="0 0 14 14"><rect width="14" height="14" rx="2" fill="var(--blue)"/><rect x="4" y="2" width="6" height="10" rx="1" fill="none" stroke="#fff" stroke-width="1.3"/></svg>
      0476 581 904
    </li>
    <li>
      <svg width="14" height="14" viewBox="0 0 14 14"><rect width="14" height="14" rx="2" fill="var(--blue)"/><rect x="2.5" y="4" width="9" height="6.5" fill="none" stroke="#fff" stroke-width="1.2"/><path d="M2.5,4 L7,8 L11.5,4" fill="none" stroke="#fff" stroke-width="1.2"/></svg>
      marisol@dawnquill.com
    </li>
    <li>
      <svg width="14" height="14" viewBox="0 0 14 14"><rect width="14" height="14" rx="2" fill="var(--blue)"/></svg>
      /dawnquill101
    </li>
    <li>
      <svg width="14" height="14" viewBox="0 0 14 14"><rect width="14" height="14" rx="2" fill="var(--blue)"/><circle cx="7" cy="7" r="4.5" fill="none" stroke="#fff" stroke-width="1.1"/><path d="M2.5,7 H11.5 M7,2.5 C4.5,5 4.5,9 7,11.5 M7,2.5 C9.5,5 9.5,9 7,11.5" fill="none" stroke="#fff" stroke-width="1"/></svg>
      www.dawnquill.com
    </li>
  </ul>

  <div class="slogan">Wellness - Success - Peace of Mind</div>
</section>

</body>
</html>
```